Business Cards and Stationary for Dental Office
Brodley Dental
Use same font as used in my logo
R.T. Brodley
D.D.S, P.C.
418 West R. Parkway
Harlow, MO 65099
rtb@brodleydentalcare.test
www.brodleydentalcare.test
We are looking for clean, simple, professional designs. In addition to Business Card Design we would also like to see designs for letterhead and Envelope.

```html
<!DOCTYPE html>
<html lang="en">
<head>
<meta charset="utf-8">
<title>Brodley Dental – Business Card</title>
<link href="https://fonts.googleapis.com/css2?family=Cinzel:wght@400&family=Tinos:ital@0;1&display=swap" rel="stylesheet">
<style>
  :root {
    --green: #2fa84f;
    --green-light: #4cc66a;
    --green-dark: #1f8a3c;
    --white: #ffffff;
    --grey: #5d5f60;
    --page: #eef0ef;
  }
  * { margin: 0; padding: 0; box-sizing: border-box; }
  html, body { width: 1200px; height: 1009px; overflow: hidden; background: var(--page); }
  body { position: relative; font-family: "Tinos", "Times New Roman", serif; }

  .card {
    position: absolute;
    left: 200px;
    width: 800px;
    height: 457px;
    border-radius: 22px;
    overflow: hidden;
    box-shadow: 0 6px 18px rgba(0,0,0,.15);
  }
  .card--front { top: 27px; background: radial-gradient(ellipse at 50% 40%, var(--green-light), var(--green) 55%, var(--green-dark)); }
  .card--back { top: 524px; background: var(--green); }

  /* front */
  .front-brand { position: absolute; inset: 0; display: flex; flex-direction: column; align-items: center; justify-content: center; color: var(--white); }
  .front-brand__dot { width: 92px; height: 92px; border-radius: 50%; background: var(--white); margin-bottom: 22px; }
  .brand-name { font-family: "Cinzel", "Times New Roman", serif; font-weight: 400; letter-spacing: 1px; white-space: nowrap; }
  .front-brand .brand-name { font-size: 48px; line-height: 1; }
  .front-brand__tagline { font-style: italic; font-size: 20px; margin-top: 6px; }
  .front-brand__web { font-size: 17px; letter-spacing: 3px; margin-top: 8px; }

  /* back */
  .back-shape { position: absolute; inset: 0; }
  .back-brand { position: absolute; left: 34px; top: 154px; display: flex; flex-direction: column; }
  .back-brand__row { display: flex; align-items: center; gap: 10px; }
  .back-brand__dot { width: 42px; height: 42px; border-radius: 50%; background: var(--grey); flex: none; }
  .back-brand .brand-name { font-size: 28px; color: var(--green); line-height: 1; }
  .back-brand__tagline { font-style: italic; font-size: 16px; color: var(--green); margin: 6px 0 0 52px; border-top: 1px solid var(--green); padding-top: 3px; width: 230px; }

  .contact { position: absolute; right: 40px; top: 96px; color: var(--white); text-align: right; font-size: 19px; line-height: 1.28; }
  .contact__name { margin-bottom: 58px; letter-spacing: .5px; }
  .contact__address { margin-bottom: 18px; }
  .contact__line { display: flex; justify-content: flex-end; align-items: center; gap: 10px; }
  .contact__line svg { width: 14px; height: 14px; flex: none; }
</style>
</head>
<body>

<section class="card card--front" aria-label="Card front">
  <div class="front-brand">
    <div class="front-brand__dot"></div>
    <div class="brand-name">BRODLEY DENTAL</div>
    <div class="front-brand__tagline">a family practice</div>
    <div class="front-brand__web">www.brodleydentalcare.test</div>
  </div>
</section>

<section class="card card--back" aria-label="Card back">
  <svg class="back-shape" viewBox="0 0 800 457" preserveAspectRatio="none">
    <path d="M0,0 H318 C470,60 505,320 352,457 H0 Z" fill="var(--grey)"/>
    <path d="M0,0 H296 C440,60 470,310 325,457 H0 Z" fill="var(--white)"/>
  </svg>

  <div class="back-brand">
    <div class="back-brand__row">
      <div class="back-brand__dot"></div>
      <div class="brand-name">BRODLEY DENTAL</div>
    </div>
    <div class="back-brand__tagline">a family practice</div>
  </div>

  <div class="contact">
    <div class="contact__name">R.T. Brodley, D.D.S, P.C.</div>
    <div class="contact__address">418 West R. Parkway<br>Harlow, MO 65099</div>
    <div class="contact__line">816-555-0142
      <svg viewBox="0 0 14 14"><path d="M3 1l2 3-1.5 1.5a7 7 0 0 0 5 5L10 9l3 2-1 2C6 13 1 8 1 2z" fill="var(--white)"/></svg></div>
    <div class="contact__line">816-555-0187
      <svg viewBox="0 0 14 14"><rect x="2" y="3" width="10" height="8" rx="1" fill="var(--white)"/></svg></div>
    <div class="contact__line">rtb@brodleydentalcare.test
      <svg viewBox="0 0 14 14"><rect x="1" y="3" width="12" height="8" fill="var(--white)"/><path d="M1 3l6 5 6-5" stroke="var(--green)" fill="none"/></svg></div>
    <div class="contact__line">www.brodleydentalcare.test
      <svg viewBox="0 0 14 14"><circle cx="7" cy="7" r="6" fill="var(--white)"/></svg></div>
  </div>
</section>

</body>
</html>
```